distributor of aftermarket auto electrical components

I am after business card design for my new company called
Summit Vehicle Supplies (SVS as the acronym). I will supplying automotive wiring components, basically from battery to headlight. I will be aiming to sell in the 4wd scene and to auto electricians. i am not worried which colours are used though i would like it to be dynamic.
Updates

sorry guys, i have add a mobile and e-mail address that will need to on there as well. Sorry for theĀ inconvenience.

sorry guys i had erred on my spelling with my e-mail. i have now fixed it in the brief

Target Market(s)

4wd industry, custom cars, RV, auto electricians

Industry/Entity Type

Electrical

Requirements
Must have
• Company Name
ABN number: 71 306 548 290
Director: Derek Holloway
M 0432 718 946
E dhollo@fernwire.com.au

```html
<!DOCTYPE html>
<html lang="en">
<head>
<meta charset="utf-8">
<title>Summit Vehicle Supplies – Business Card</title>
<link href="https://fonts.googleapis.com/css2?family=Cinzel:wght@400;600&display=swap" rel="stylesheet">
<style>
  :root {
    --page-bg: #e4e7e8;
    --teal-dark: #2f8f8c;
    --teal-mid: #5ab5b0;
    --teal-light: #8fd3cc;
    --card-black: #0b0c0d;
    --wave-grey: #1f2224;
    --ink-white: #ffffff;
    --ink-teal: #8fd6d0;
    --ink-grey: #9aa0a3;
  }
  * { margin: 0; padding: 0; box-sizing: border-box; }
  html, body { width: 1200px; height: 671px; overflow: hidden; }
  body {
    background: var(--page-bg);
    font-family: "Cinzel", "Times New Roman", serif;
    position: relative;
  }
  .business-card {
    position: absolute;
    left: 390px;
    top: 85px;
    width: 420px;
    height: 500px;
    overflow: hidden;
    box-shadow: 0 10px 30px rgba(0,0,0,0.25);
  }
  .card-background { position: absolute; inset: 0; width: 100%; height: 100%; }
  .company-name {
    position: absolute;
    top: 58px;
    width: 100%;
    text-align: center;
    font-size: 22px;
    letter-spacing: 0.5px;
    color: var(--ink-white);
    text-shadow: 0 1px 2px rgba(0,0,0,0.55);
  }
  .person {
    position: absolute;
    top: 268px;
    width: 100%;
    text-align: center;
  }
  .person-name {
    font-size: 40px;
    color: var(--ink-white);
    letter-spacing: 0.5px;
    line-height: 1;
  }
  .person-title {
    font-size: 9px;
    color: var(--ink-grey);
    letter-spacing: 1px;
    margin-top: 6px;
  }
  .title-rule {
    display: block;
    margin: 10px auto 0;
    width: 150px;
    height: 3px;
    border-radius: 50%;
    background: radial-gradient(ellipse at center, var(--teal-light) 0%, rgba(143,211,204,0) 75%);
  }
  .contact-details {
    position: absolute;
    top: 398px;
    width: 100%;
    text-align: center;
    font-size: 12.5px;
    line-height: 1.85;
    color: var(--ink-teal);
  }
  .contact-email { color: var(--ink-white); }
</style>
</head>
<body>
  <article class="business-card">
    <svg class="card-background" viewBox="0 0 420 500" preserveAspectRatio="none" aria-hidden="true">
      <defs>
        <linearGradient id="tealFade" x1="0" y1="0" x2="0" y2="1">
          <stop offset="0" stop-color="var(--teal-dark)"/>
          <stop offset="1" stop-color="var(--teal-mid)"/>
        </linearGradient>
      </defs>
      <rect width="420" height="500" fill="url(#tealFade)"/>
      <g fill="#ffffff" opacity="0.06">
        <rect x="0" y="0" width="60" height="260"/>
        <rect x="120" y="0" width="60" height="260"/>
        <rect x="240" y="0" width="60" height="260"/>
        <rect x="360" y="0" width="60" height="260"/>
      </g>
      <path d="M0 190 C110 230 230 215 420 200 L420 260 L0 260 Z" fill="var(--teal-light)" opacity="0.55"/>
      <path d="M0 285 C120 250 260 225 420 232 L420 500 L0 500 Z" fill="var(--wave-grey)"/>
      <path d="M0 300 C130 268 270 250 420 258 L420 500 L0 500 Z" fill="var(--card-black)"/>
    </svg>

    <h1 class="company-name">Summit Vehicle Supplies</h1>

    <div class="person">
      <p class="person-name">Derek Holloway</p>
      <p class="person-title">Director</p>
      <span class="title-rule"></span>
    </div>

    <address class="contact-details" style="font-style: normal;">
      <p>1234, Adress Lane Adress City, &nbsp;EX 12345</p>
      <p>ABN Number: 71 306 548 290 &nbsp;Cell Phone: 0432 718 946</p>
      <p class="contact-email">dhollo@fernwire.com.au</p>
    </address>
  </article>
</body>
</html>
```